Venneputt.dk - FriendPutt

I need a design for a WordPress site that serves to inform and present the national golfchampionship for colleagues in Denmark. The sites need to be visual stuninng or big, and it doesnt have a lot of pages. Maybe 5-6 regular text pages and not a lot of navigation. It should be a simple and powerfull site.

The sites need to present and sell the tournament, and have a clear call to action button "Sign up" (Tilmeld) and resultscoring.

If you can make a logo and visual ID for the tournament as well that would be a bonus.

Target Market(s)

Golfers

Logo Text

Venneputt

Number of Pages Required

3 page

Requirements
Must have
• A frontpage
• Button 1 - Tilmeld (danish for sign up)
• Button 2 - Resultater (results)
Nice to have
• Logo
• A style we can use offline as well

```html
<!DOCTYPE html>
<html lang="da">
<head>
<meta charset="utf-8">
<title>Venneputt.dk – FriendPutt</title>
<link href="https://fonts.googleapis.com/css2?family=Open+Sans:ital,wght@0,400;0,600;0,700;0,800;1,700&display=swap" rel="stylesheet">
<style>
:root{
  --red:#e3001b;
  --yellow:#ffd400;
  --blue:#1b7fc4;
  --ink:#3a3a3a;
  --muted:#6b6b6b;
  --line:#dcdcdc;
  --footer:#f0f0f0;
  --grass:#6f8f3a;
  --sky:#b9c7c2;
}
*{box-sizing:border-box;margin:0;padding:0}
html,body{width:673px;height:1200px;overflow:hidden}
body{font-family:"Open Sans",Arial,sans-serif;color:var(--ink);background:#fff;position:relative}
.btn{display:inline-flex;align-items:center;gap:10px;font-weight:700;font-size:13px;text-transform:uppercase;text-decoration:none;padding:0 14px;height:32px;border-radius:2px}
.btn--red{background:var(--red);color:#fff}
.btn--yellow{background:var(--yellow);color:#222}
.btn svg{width:20px;height:12px}

/* header */
.site-header{height:52px;display:flex;align-items:center;padding:0 14px;gap:10px}
.brand{width:190px}
.brand__name{font-size:13px;font-weight:700;color:var(--ink);white-space:nowrap}
.nav{display:flex;gap:12px;font-size:10px;font-weight:600;color:#444;text-transform:uppercase;flex:1}
.site-header .btn{height:28px;font-size:11px;padding:0 12px}

/* hero */
.hero{position:relative;height:378px;background:linear-gradient(180deg,var(--sky) 0%,#9fb0a8 40%,var(--grass) 75%,#566f2c 100%)}
.hero__panel{position:absolute;left:234px;top:35px;width:208px;padding:18px 14px;background:rgba(20,20,20,.72);text-align:center}
.hero__title{color:var(--yellow);font-size:20px;font-weight:600;line-height:1.25}
.hero__dates{color:#fff;font-size:12px;margin-top:18px;line-height:1.4}
.hero__cta{position:absolute;left:0;right:0;top:318px;display:flex;justify-content:center;gap:14px}
.hero__cta .btn{height:36px;padding:0 20px;font-size:14px}

/* blue band */
.band{height:60px;background:var(--blue);display:flex;align-items:center;padding:0 14px;gap:24px;color:#fff}
.band__tag{background:#fff;color:var(--blue);font-style:italic;font-weight:700;font-size:18px;padding:6px 12px}
.band__text{font-size:10px;line-height:1.4;width:230px}
.band__link{font-size:10px;line-height:1.4}

/* photos */
.gallery{display:flex;gap:4px;height:152px;margin-top:4px}
.gallery__item{flex:1;background:linear-gradient(180deg,#c9d3c6 0%,#86a356 55%,#5c7a30 100%)}
.gallery__item:nth-child(2){background:linear-gradient(180deg,#b8c6c2 0%,#7c9a4b 55%,#4e6d28 100%)}

/* features */
.features{display:grid;grid-template-columns:repeat(3,1fr);column-gap:24px;padding:22px 38px 0}
.feature{border-bottom:1px solid var(--line);padding-bottom:14px;margin-bottom:18px;min-height:130px}
.feature h2{color:var(--blue);font-size:15px;font-weight:600;line-height:1.3;margin-bottom:12px}
.feature p{font-size:9.5px;line-height:1.55;color:var(--muted)}
.feature--row2{border-bottom:none;min-height:120px}
.feature .feature__price{font-size:14px;line-height:1.3;color:var(--ink);margin-top:0}
.cta-row{display:flex;justify-content:center;gap:14px;margin-top:4px}
.cta-row .btn{height:36px;padding:0 20px;font-size:14px}

/* footer */
.site-footer{position:absolute;left:0;right:0;bottom:0;height:146px;background:var(--footer);border-top:4px solid var(--red);padding:18px 38px 0}
.footer__grid{display:flex;gap:22px}
.partners{display:flex;gap:10px;width:130px}
.partner{width:44px;height:40px;background:#d7d7d7;border-radius:3px}
.partner--wide{width:66px}
.contact{display:grid;grid-template-columns:1fr 1fr;row-gap:14px;column-gap:14px;font-size:10px;color:var(--muted);width:220px}
.contact__item{display:flex;gap:6px}
.contact__item svg{width:14px;height:14px;flex:none}
.contact__label{font-size:8px;display:block}
.contact__mail{font-size:10px;color:var(--muted)}
.newsletter{display:inline-block;background:var(--red);color:#fff;font-size:8px;font-weight:700;padding:4px 8px;border-radius:2px;text-transform:uppercase;margin-top:8px}
.social{display:flex;gap:6px;margin-top:8px}
.social span{width:16px;height:16px;border:1px solid #888;border-radius:50%}
.copyright{position:absolute;left:0;right:0;bottom:10px;text-align:center;font-size:8px;color:#999}
</style>
</head>
<body>

<header class="site-header">
  <div class="brand">
    <span class="brand__name">Dansk Venneidræt</span>
  </div>
  <nav class="nav"><span>Home</span><span>About us</span><span>Tournament</span><span>Contact us</span></nav>
  <a class="btn btn--red" href="#">Tilmeld</a>
  <a class="btn btn--yellow" href="#">Resultater</a>
</header>

<section class="hero" role="img" aria-label="Golfspiller på green med flag og klubbe">
  <div class="hero__panel">
    <p class="hero__title">Lav et hold og kom rundt på de danske golfbaner i venneidrættens sjove holdturnering!</p>
    <p class="hero__dates">Turneringsstart<br>den 22. april – Finalestævne<br>den 21. september</p>
  </div>
  <div class="hero__cta">
    <a class="btn btn--red" href="#">Tilmeld <svg viewBox="0 0 20 12"><path d="M0 6h17M12 1l6 5-6 5" stroke="#fff" stroke-width="2" fill="none"/></svg></a>
    <a class="btn btn--yellow" href="#">Resultater <svg viewBox="0 0 20 12"><path d="M0 6h17M12 1l6 5-6 5" stroke="#222" stroke-width="2" fill="none"/></svg></a>
  </div>
</section>

<section class="band">
  <span class="band__tag">Freelance-golfer?</span>
  <p class="band__text">Vil du deltage i Danmarks største landsdækkende Pay and Play turnering for hold.</p>
  <p class="band__link">Se mere på<br>www.spilendag.dk</p>
</section>

<div class="gallery">
  <div class="gallery__item" role="img" aria-label="Golfspiller putter på green"></div>
  <div class="gallery__item" role="img" aria-label="Hold af kolleger på golfbanen"></div>
  <div class="gallery__item" role="img" aria-label="Spillere ved hul med flag"></div>
</div>

<section class="features">
  <article class="feature">
    <h2>Hold på 2-4 spillere</h2>
    <p>Et hold består af 2-4 spillere. Hver runde spilles som holdmatch, hvor de to bedste scorer tæller. Alle niveauer kan deltage, og I vælger selv jeres holdkaptajn.</p>
  </article>
  <article class="feature">
    <h2>Bestem selv, hvor og hvornår matchen skal spilles</h2>
    <p>I Venneputt.dk finder I modstandere i jeres egen region. Aftal dato og bane direkte med det andet hold, og indberet resultatet online bagefter. Alle runder skal være spillet inden 1. september.</p>
  </article>
  <article class="feature">
    <h2>Tilmeld jer senest den 15. april</h2>
    <p>Tag fat i jeres kolleger og tilmeld holdet på www.venneputt.dk – senest den 15. april 2013.</p>
  </article>
  <article class="feature feature--row2">
    <h2>Finalestævne på Havbakke Golfbane</h2>
    <p>Vinderne fra hver pulje inviteres til finalestævnet, som spilles den 21. september på Havbakke Golfbane. Her kåres årets danske mestre.</p>
  </article>
  <article class="feature feature--row2">
    <h2>1. præmie: Weekendophold for hele holdet på Nordstrand Golf Resort</h2>
  </article>
  <article class="feature feature--row2">
    <p class="feature__price">Kr. 600,- pr. hold</p>
  </article>
</section>

<div class="cta-row">
  <a class="btn btn--red" href="#">Tilmeld <svg viewBox="0 0 20 12"><path d="M0 6h17M12 1l6 5-6 5" stroke="#fff" stroke-width="2" fill="none"/></svg></a>
  <a class="btn btn--yellow" href="#">Resultater <svg viewBox="0 0 20 12"><path d="M0 6h17M12 1l6 5-6 5" stroke="#222" stroke-width="2" fill="none"/></svg></a>
</div>

<footer class="site-footer">
  <div class="footer__grid">
    <div class="partners">
      <span class="partner"></span>
      <span class="partner partner--wide"></span>
    </div>
    <div class="contact">
      <div class="contact__item">
        <svg viewBox="0 0 14 14"><path d="M3 1h3l1 3-2 1a7 7 0 0 0 4 4l1-2 3 1v3a1 1 0 0 1-1 1A11 11 0 0 1 2 2a1 1 0 0 1 1-1z" fill="#888"/></svg>
        <div><span class="contact__label">Tlf.</span>40 12 34 56</div>
      </div>
      <div><span class="contact__label">Fax</span>40 12 34 57</div>
      <div class="contact__item">
        <svg viewBox="0 0 14 14"><path d="M7 1a4 4 0 0 1 4 4c0 3-4 8-4 8S3 8 3 5a4 4 0 0 1 4-4z" fill="#888"/><circle cx="7" cy="5" r="1.5" fill="#f0f0f0"/></svg>
        <div><span class="contact__label">Adresse</span>Skovvej 14<br>5800 Nyborg</div>
      </div>
    </div>
    <div>
      <div class="contact__item">
        <svg viewBox="0 0 14 14"><rect x="1" y="3" width="12" height="8" fill="none" stroke="#888"/><path d="M1 3l6 5 6-5" fill="none" stroke="#888"/></svg>
        <div><span class="contact__label">E-mail</span><span class="contact__mail">kontakt@venneidraet.dk</span></div>
      </div>
      <span class="newsletter">Nyhedsbrev</span>
      <div class="social"><span></span><span></span></div>
    </div>
  </div>
  <p class="copyright">© 2013 venneidraet.dk. All rights reserved.</p>
</footer>

</body>
</html>
```